Do me a Simple layout and Blow the stockings off my clients!!

I am a Personal Stylist focusing on helping women/mothers needing to revamp their wardrobe and feel confident and fresh again. I'm receiving very positive feedback and growing interest in the services I offer. I provide a 'Client Profile' as part of that service in a word document (saved as PDF). What I'm needing is to turn the average looking word document into a modern, funky and professional document template. I have a business logo and copy.
The template should be fluid, easy to update and communicate sassy, funky and professional.

Target Market(s)

Females 25-65.

Industry/Entity Type

Business

Font styles to use
Other font styles liked:
• HelveticaNeue Condensed, or Raleway

Requirements
Must have
• Colours and styles consistent with logo, and fashion industry.
• Interesting and emotive elements around the content.
• Create clear 'sections' with high impact (full coloured page with single, simple section heading ?)
Nice to have
• Ability to feature 'subjects' photos in interesting ways through out the document.
• Don't just stick with portrait layout, landscape is fine too.
Should not have
• Not too busy - less is more.

```html
<!DOCTYPE html>
<html lang="en">
<head>
<meta charset="utf-8">
<title>Stylist Report Template – Headers and Footer</title>
<link rel="stylesheet" href="https://fonts.googleapis.com/css2?family=Arimo:wght@700&family=Dancing+Script:wght@400&display=swap">
<style>
  :root {
    --ink-frame: #1a1a1a;
    --paper: #ffffff;
    --label-grey: #b5b5b5;
    --ribbon-pink: #ff0a94;
    --ribbon-plum: #5a0a38;
    --fold-shadow: #3e0526;
    --stitch: #ffffff;
    --brand-pink: #d6338a;
    --strip-pink: #f3a3c8;
    --strip-magenta: #c4157a;
    --strip-grey: #c9c9c9;
  }
  html, body {
    margin: 0;
    padding: 0;
    overflow: hidden;
    background: var(--paper);
  }
  .sheet {
    position: relative;
    width: 1200px;
    height: 881px;
    box-sizing: border-box;
    border: 2px solid var(--ink-frame);
    background: var(--paper);
    overflow: hidden;
  }
  .swatch-defs {
    position: absolute;
    width: 0;
    height: 0;
  }
  .header-block {
    position: absolute;
    left: 0;
    width: 1196px;
    height: 130px;
  }
  .header-block--one   { top: 87px; }
  .header-block--two   { top: 272px; }
  .header-block--three { top: 462px; }
  .ribbon-art {
    position: absolute;
    left: 0;
    top: 0;
    width: 960px;
    height: 110px;
  }
  .block-label,
  .footer-label {
    position: absolute;
    margin: 0;
    font-family: "Arimo", Arial, sans-serif;
    font-weight: 700;
    font-size: 27px;
    line-height: 1;
    color: var(--label-grey);
  }
  .block-label { left: 444px; top: 0; }
  .ribbon-title {
    position: absolute;
    right: calc(1196px - 869px);
    top: 57px;
    margin: 0;
    font-family: "Dancing Script", cursive;
    font-weight: 400;
    font-size: 22px;
    line-height: 1;
    color: var(--stitch);
    white-space: nowrap;
  }
  .brand-name {
    position: absolute;
    left: 966px;
    top: 8px;
    width: 190px;
    margin: 0;
    font-family: "Arimo", Arial, sans-serif;
    font-weight: 700;
    font-size: 28px;
    line-height: 34px;
    color: var(--brand-pink);
    text-align: center;
  }
  .brand-name span { display: block; }
  .brand-name .brand-stylist {
    margin-top: 6px;
    font-size: 12px;
    line-height: 14px;
    letter-spacing: 0.5px;
    text-align: right;
    text-transform: uppercase;
  }
  .footer-label { left: 38px; top: 690px; }
  .footer-strip {
    position: absolute;
    left: 18px;
    top: 752px;
    width: 1158px;
    height: 36px;
    background: linear-gradient(90deg,
      var(--strip-grey) 0%, var(--strip-magenta) 12%, var(--strip-pink) 25%,
      var(--strip-grey) 37%, var(--strip-magenta) 50%, var(--strip-pink) 62%,
      var(--strip-grey) 75%, var(--strip-magenta) 87%, var(--strip-pink) 100%);
    opacity: 0.55;
  }
</style>
</head>
<body>
<main class="sheet">

  <svg class="swatch-defs" aria-hidden="true" focusable="false">
    <defs>
      <linearGradient id="ribbonFade" x1="0" y1="0" x2="1" y2="0">
        <stop offset="0" stop-color="#ff0a94"/>
        <stop offset="0.35" stop-color="#e6067f"/>
        <stop offset="1" stop-color="#5a0a38"/>
      </linearGradient>
    </defs>
  </svg>

  <section class="header-block header-block--one" aria-label="Header style one">
    <svg class="ribbon-art" viewBox="0 0 960 110" aria-hidden="true">
      <rect x="18" y="0" width="393" height="57" fill="url(#ribbonFade)"/>
      <line x1="20" y1="5" x2="409" y2="5" stroke="#fff" stroke-width="1.6" stroke-dasharray="1.6 4.2"/>
      <line x1="20" y1="52" x2="409" y2="52" stroke="#fff" stroke-width="1.6" stroke-dasharray="1.6 4.2"/>
      <polygon points="371,57 411,24 411,57" fill="#3e0526"/>
      <polygon points="371,41 948,41 912,70 948,99 371,99" fill="url(#ribbonFade)"/>
      <line x1="373" y1="46" x2="938" y2="46" stroke="#fff" stroke-width="1.6" stroke-dasharray="1.6 4.2"/>
      <line x1="373" y1="94" x2="938" y2="94" stroke="#fff" stroke-width="1.6" stroke-dasharray="1.6 4.2"/>
    </svg>
    <h2 class="block-label">header1</h2>
    <p class="ribbon-title">Style Analysis Report</p>
    <p class="brand-name"><span>Satchels &amp;</span><span>Stilettos</span><span class="brand-stylist">Lena Marlow</span></p>
  </section>

  <section class="header-block header-block--two" aria-label="Header style two">
    <svg class="ribbon-art" viewBox="0 0 960 110" aria-hidden="true">
      <rect x="18" y="0" width="393" height="57" fill="url(#ribbonFade)"/>
      <line x1="20" y1="5" x2="409" y2="5" stroke="#fff" stroke-width="1.6" stroke-dasharray="1.6 4.2"/>
      <line x1="20" y1="52" x2="409" y2="52" stroke="#fff" stroke-width="1.6" stroke-dasharray="1.6 4.2"/>
      <polygon points="371,57 411,24 411,57" fill="#3e0526"/>
      <polygon points="371,41 948,41 912,70 948,99 371,99" fill="url(#ribbonFade)"/>
      <line x1="373" y1="46" x2="938" y2="46" stroke="#fff" stroke-width="1.6" stroke-dasharray="1.6 4.2"/>
      <line x1="373" y1="94" x2="938" y2="94" stroke="#fff" stroke-width="1.6" stroke-dasharray="1.6 4.2"/>
    </svg>
    <h2 class="block-label">header2</h2>
    <p class="ribbon-title">Notes from your styling session</p>
    <p class="brand-name"><span>Satchels &amp;</span><span>Stilettos</span><span class="brand-stylist">Lena Marlow</span></p>
  </section>

  <section class="header-block header-block--three" aria-label="Header style three">
    <svg class="ribbon-art" viewBox="0 0 960 110" aria-hidden="true">
      <rect x="18" y="0" width="393" height="57" fill="url(#ribbonFade)"/>
      <line x1="20" y1="5" x2="409" y2="5" stroke="#fff" stroke-width="1.6" stroke-dasharray="1.6 4.2"/>
      <line x1="20" y1="52" x2="409" y2="52" stroke="#fff" stroke-width="1.6" stroke-dasharray="1.6 4.2"/>
      <polygon points="371,57 411,24 411,57" fill="#3e0526"/>
      <polygon points="371,41 948,41 912,70 948,99 371,99" fill="url(#ribbonFade)"/>
      <line x1="373" y1="46" x2="938" y2="46" stroke="#fff" stroke-width="1.6" stroke-dasharray="1.6 4.2"/>
      <line x1="373" y1="94" x2="938" y2="94" stroke="#fff" stroke-width="1.6" stroke-dasharray="1.6 4.2"/>
    </svg>
    <h2 class="block-label">header3</h2>
    <p class="brand-name"><span>Satchels &amp;</span><span>Stilettos</span><span class="brand-stylist">Lena Marlow</span></p>
  </section>

  <footer>
    <h2 class="footer-label">footer</h2>
    <div class="footer-strip" role="img" aria-label="Repeating border of small fashion icons: lipstick, drop earrings, handbag, dress, high heel and bracelet in pink, magenta and grey"></div>
  </footer>

</main>
</body>
</html>
```